Law firm website marketed direct to many individual clients

I need someone to design a very basic website for a law firm that will be very eye catching. It's going to be a single-paged, scrolling website with a small number of folds. I have uploaded a simple word document that outlines the basics of what I thought could be the layout, but I am open to suggestion on font, size, shades of color, organization, etc. etc. Essentially the website just needs to be a very efficient and visually appealing way of conveying some simple messages.

Target Market(s)

High volumes of individuals who have gotten into a car accident and then google on their phones a lawyer to hire to represent them.

Industry/Entity Type

Legal

Number of Pages Required

1 page

Font styles to use
Serif
Sans Serif

Colors
34a7d7
85cae6
0592cd

Requirements
Must have
• Must be bright and grab the users attention with color scheme and layout. The different sections should be done in such a way that they can fit entirely onto one smart phone or tablet screen.
Nice to have
• I'd like to try and see what it looks like if in the middle somewhere there is a fold that says "MEET YOUR ATTORNEYS" and includes individual photos of two attorneys, one on the left side and one on the right. And then a small bio section on them. I don't want the photos to include a square or rectangle background, I want the person in the photo to be superimposed on top of whatever pattern or background you have in the fold.
Should not have
• Do not want too much text. Anything more than 2 sentences in any single place is unacceptable.

```html
<!DOCTYPE html>
<html lang="en">
<head>
<meta charset="utf-8">
<title>Meridian Law Group</title>
<link href="https://fonts.googleapis.com/css2?family=Oswald:wght@300;400&family=Open+Sans:wght@400;600;700&display=swap" rel="stylesheet">
<style>
:root{
  --blue:#0592cd;
  --sky:#34a7d7;
  --pale:#85cae6;
  --navy:#0d5c96;
  --ink:#1e3c5a;
  --text:#555;
  --rule:#e6e6e6;
  --footer:#3aa6d8;
  --footer-dark:#0a87c6;
  --footer-light:#7fc6e6;
}
*{box-sizing:border-box;margin:0;padding:0}
html,body{width:1200px;height:2894px;overflow:hidden}
body{position:relative;background:#fff;font-family:"Open Sans",Arial,sans-serif;color:var(--text)}
.abs{position:absolute}
.display{font-family:"Oswald","Arial Narrow",sans-serif;font-weight:300;line-height:1.2}

/* header */
.site-header{top:0;left:0;width:1200px;height:93px;background:#fff}
.brand{left:73px;top:22px;font-size:34px;font-weight:700;color:var(--sky);letter-spacing:-.5px}
.header-phone{right:70px;top:26px;display:flex;align-items:center;gap:12px;font-size:25px;font-weight:700;color:var(--sky)}

/* hero */
.hero{top:93px;left:0;width:1200px;height:625px}
.hero-bg{position:absolute;inset:0;background:linear-gradient(180deg,#3aa3dc 0%,#2f9ad6 50%,#2b95d2 100%)}
.hero-kicker{top:48px;left:0;width:1200px;text-align:center;font-size:32px;color:#fff;font-weight:400;line-height:40px}
.hero-sub{top:220px;left:400px;width:400px;text-align:center;font-size:40px;color:#fff;line-height:44px}
.hero-title{top:258px;left:300px;width:600px;text-align:center;font-size:66px;color:#fff;font-weight:400;line-height:70px}

.call-btn{display:flex;align-items:center;justify-content:center;width:204px;height:42px;background:var(--pale);color:var(--ink);font-size:20px;font-weight:600;border-radius:3px}

.lead-form{left:793px;top:142px;width:332px;height:325px}
.lead-form .head{position:absolute;top:0;left:0;width:332px;height:110px;background:#1c8dd0;border-radius:6px 6px 0 0;padding:14px 18px;color:#fff;font-size:25px;font-weight:600;line-height:1.2}
.lead-form .body{position:absolute;top:80px;left:0;width:332px;height:245px;background:#fff;border-radius:32px 30px 6px 6px;box-shadow:0 2px 6px rgba(0,0,0,.2);padding:28px 18px 0}
.field{height:36px;background:#e6e6e6;border-radius:3px;margin-bottom:10px;display:flex;align-items:center;justify-content:space-between;padding:0 12px;font-size:14px;color:#777}
.submit{height:42px;background:var(--pale);border-radius:3px;display:flex;align-items:center;justify-content:center;font-size:16px;font-weight:700;color:var(--ink);margin-top:4px}
.learn-more{left:545px;top:573px;width:111px;height:52px;background:#1f6fa8;color:#fff;text-align:center;font-size:13px;font-weight:700;padding-top:8px}

/* features */
.feature{left:0;width:1200px;height:152px;border-bottom:3px solid var(--rule)}
.feature .icon{position:absolute;left:260px;top:14px;width:125px;height:125px;border-radius:50%;background:var(--pale)}
.feature h3{position:absolute;left:402px;top:44px;font-size:29px;font-weight:600;color:var(--blue)}
.feature p{position:absolute;left:402px;top:84px;font-size:16px;color:#666}

/* band */
.band{left:0;top:1437px;width:1200px;height:595px}
.band-title{left:0;width:1200px;text-align:center;font-size:58px;color:#fff;font-weight:300;z-index:2}
.band-text{text-align:center;color:#fff;font-size:16px;line-height:1.5;z-index:2}
.band-photo{left:1000px;top:1610px;width:200px;height:384px;background:linear-gradient(180deg,#c9b4a3 0%,#6b7a8c 40%,#1c2430 100%);border-radius:100px 100px 0 0;z-index:1}

/* attorneys */
.section-label{left:0;width:1200px;text-align:center}
.label-meet{display:inline-block;background:var(--blue);color:#fff;font-size:29px;font-weight:600;padding:0 12px;line-height:38px}
.label-sub{font-size:30px;font-weight:600;color:var(--blue);margin-top:2px}
.attorney-photo{width:243px;height:325px;background:linear-gradient(180deg,#e8eef2 0%,#b9c4cc 55%,#4a5562 100%)}
.attorney{width:250px}
.attorney h4{font-family:"Oswald","Arial Narrow",sans-serif;font-weight:300;font-size:27px;color:var(--blue)}
.attorney .role{font-size:13px;font-weight:700;color:#666;margin-top:-2px}
.attorney .years{font-size:13px;color:var(--sky);margin-top:18px}
.attorney p{font-size:14px;line-height:1.75;color:#444;margin-top:10px}
.attorney .more{font-size:14px;color:var(--blue);margin-top:12px}

/* footer */
.social-bar{left:0;top:2608px;width:1200px;height:43px;background:var(--footer-dark);display:flex;align-items:center;gap:30px;padding-left:70px;color:#fff;font-size:12px;font-weight:600}
.social-bar span{display:flex;align-items:center;gap:10px}
.social-dot{width:28px;height:28px;border:2px solid #fff;border-radius:50%}
.footer-main{left:0;top:2651px;width:1200px;height:198px;background:var(--footer)}
.footer-col{top:2680px;color:#fff}
.footer-col h5{font-size:16px;font-weight:700;padding-bottom:8px;border-bottom:1px solid rgba(255,255,255,.45);width:330px}
.footer-col p{font-size:13px;line-height:1.9;margin-top:12px}
.footer-col b{font-weight:700}
.subscribe{display:flex;align-items:center;gap:12px;margin-top:14px}
.subscribe .input{width:192px;height:40px;border-radius:20px;background:#fff;color:#888;font-size:12px;padding:12px 16px}
.subscribe .go{width:42px;height:42px;border-radius:50%;border:2px solid #fff}
.footer-bottom{left:0;top:2849px;width:1200px;height:45px;background:var(--footer-light);color:var(--ink);font-size:12px;display:flex;align-items:center;justify-content:space-between;padding:0 70px}
.footer-bottom nav{display:flex;gap:30px}
</style>
</head>
<body>

<header class="site-header abs">
  <div class="brand abs">MERIDIAN LAW GROUP</div>
  <div class="header-phone abs">
    <svg width="34" height="34" viewBox="0 0 34 34"><circle cx="17" cy="17" r="15" fill="none" stroke="#34a7d7" stroke-width="2.5"/><path d="M11 9c2-1 3 2 4 4s-2 2-1 4 3 4 5 4 2-3 4-2 3 2 2 4-4 3-8 0-8-9-6-14z" fill="#34a7d7"/></svg>
    555-014-2290
  </div>
</header>

<section class="hero abs">
  <div class="hero-bg" role="img" aria-label="Courthouse columns seen from below, tinted blue"></div>
  <svg class="abs" style="left:0;bottom:0" width="1200" height="42" viewBox="0 0 1200 42"><polygon points="0,0 600,42 1200,0 1200,42 0,42" fill="#fff"/></svg>
  <div class="hero-kicker abs display">ACCIDENT? INJURED?</div>
  <div class="hero-sub abs display">YOUR CASE</div>
  <div class="hero-title abs display">YOUR MONEY</div>
  <svg class="abs" style="left:585px;top:433px" width="32" height="32" viewBox="0 0 32 32"><circle cx="16" cy="16" r="14" fill="#85cae6" stroke="#1e3c5a" stroke-width="2"/><path d="M11 9c2-1 3 2 3 4s-1 2 0 4 3 3 4 3 2-2 4-1 2 2 1 3-3 3-7 0-7-9-5-13z" fill="#1e3c5a"/></svg>
  <div class="call-btn abs" style="left:498px;top:453px">CALL 555-014-2290</div>

  <form class="lead-form abs">
    <div class="head">FIND OUT WHAT YOUR CASE IS WORTH</div>
    <div class="body">
      <div class="field">Name<span>&#9675;</span></div>
      <div class="field">Phone Number<span>&#9742;</span></div>
      <div class="field">Email<span>&#9633;</span></div>
      <div class="submit">SUBMIT</div>
    </div>
  </form>

  <div class="learn-more abs">LEARN MORE
    <svg width="22" height="22" viewBox="0 0 22 22" style="display:block;margin:4px auto 0"><circle cx="11" cy="11" r="9" fill="none" stroke="#fff" stroke-width="1.5"/><path d="M7 9l4 4 4-4" fill="none" stroke="#fff" stroke-width="1.5"/></svg>
  </div>
</section>

<section class="features">
  <div class="feature abs" style="top:772px">
    <div class="icon"><svg width="125" height="125" viewBox="0 0 125 125"><rect x="32" y="38" width="58" height="44" rx="4" fill="none" stroke="#fff" stroke-width="3"/><rect x="72" y="52" width="18" height="14" fill="none" stroke="#fff" stroke-width="3"/><circle cx="62" cy="90" r="10" fill="#fff"/><path d="M62 84v10M58 90l4 4 4-4" stroke="#85cae6" stroke-width="2.5" fill="none"/></svg></div>
    <h3>LOW FEES</h3><p>We charge less, so you keep more.</p>
  </div>
  <div class="feature abs" style="top:927px">
    <div class="icon"><svg width="125" height="125" viewBox="0 0 125 125"><circle cx="62" cy="44" r="11" fill="none" stroke="#fff" stroke-width="3"/><path d="M42 78c0-12 9-20 20-20s20 8 20 20" fill="none" stroke="#fff" stroke-width="3"/><rect x="46" y="68" width="32" height="16" fill="none" stroke="#fff" stroke-width="3"/><line x1="30" y1="88" x2="95" y2="88" stroke="#fff" stroke-width="3"/></svg></div>
    <h3>FREE CONSULTATION</h3><p>It's always free to talk to us.</p>
  </div>
  <div class="feature abs" style="top:1082px">
    <div class="icon"><svg width="125" height="125" viewBox="0 0 125 125"><circle cx="62" cy="62" r="38" fill="none" stroke="#fff" stroke-width="4"/><path d="M48 40c5-2 7 5 8 9s-4 4-2 9 7 9 11 9 4-6 9-4 8 4 6 8-8 8-17 2-18-22-15-33z" fill="#fff"/></svg></div>
    <h3>GET STARTED USING ONLY YOUR PHONE</h3><p>No need to come to the office, sign up using your phone.</p>
  </div>
  <div class="feature abs" style="top:1237px;border-bottom:none">
    <div class="icon"><svg width="125" height="125" viewBox="0 0 125 125"><circle cx="62" cy="48" r="14" fill="none" stroke="#fff" stroke-width="3"/><path d="M36 92c0-16 12-26 26-26s26 10 26 26z" fill="none" stroke="#fff" stroke-width="3"/><path d="M58 66l4 14 4-14" fill="none" stroke="#fff" stroke-width="3"/></svg></div>
    <h3>SPEAK DIRECTLY TO A LAWYER</h3><p>No staff screening. Talk right to a lawyer on your first call.</p>
  </div>
  <svg class="abs" style="left:585px;top:1369px" width="32" height="32" viewBox="0 0 32 32"><circle cx="16" cy="16" r="14" fill="#85cae6" stroke="#1e3c5a" stroke-width="2"/><path d="M11 9c2-1 3 2 3 4s-1 2 0 4 3 3 4 3 2-2 4-1 2 2 1 3-3 3-7 0-7-9-5-13z" fill="#1e3c5a"/></svg>
  <div class="call-btn abs" style="left:498px;top:1389px">CALL 555-014-2290</div>
</section>

<div class="band-photo abs" role="img" aria-label="Smiling attorney in a dark suit pointing upward"></div>
<section class="band abs">
  <svg class="abs" style="left:0;top:0" width="1200" height="595" viewBox="0 0 1200 595" role="img" aria-label="Blue backdrop with a faint statue of justice">
    <defs><linearGradient id="bandFill" x1="0" y1="0" x2="0" y2="1"><stop offset="0" stop-color="#0f5f9c"/><stop offset="1" stop-color="#0b4f86"/></linearGradient></defs>
    <polygon points="0,0 520,0 600,40 680,0 1200,0 1200,557 600,595 0,557" fill="url(#bandFill)"/>
  </svg>
  <div class="band-title abs display" style="top:134px">NO FEE UNLESS WE WIN</div>
  <div class="band-text abs" style="top:213px;left:140px;width:840px">We don't get paid unless you get paid. It's as simple as that. We let our results do the talking for us.</div>
  <div class="band-title abs display" style="top:300px">QUESTIONS ABOUT ANYTHING?</div>
  <div class="band-text abs" style="top:382px;left:140px;width:840px">We're here to help. Feel free to call us at 555-014-2290 to speak to one of our attorneys. With extensive experience in helping clients get the results that they want, our team is always just a phone call away.</div>
  <svg class="abs" style="left:585px;top:487px" width="32" height="32" viewBox="0 0 32 32"><circle cx="16" cy="16" r="14" fill="#85cae6" stroke="#1e3c5a" stroke-width="2"/><path d="M11 9c2-1 3 2 3 4s-1 2 0 4 3 3 4 3 2-2 4-1 2 2 1 3-3 3-7 0-7-9-5-13z" fill="#1e3c5a"/></svg>
  <div class="call-btn abs" style="left:498px;top:507px">CALL 555-014-2290</div>
</section>

<section class="attorneys">
  <div class="section-label abs" style="top:2106px">
    <span class="label-meet">MEET</span>
    <div class="label-sub">YOUR ATTORNEYS</div>
  </div>

  <div class="attorney-photo abs" style="left:73px;top:2218px" role="img" aria-label="Portrait of attorney Daniel Reyes"></div>
  <div class="attorney abs" style="left:343px;top:2218px">
    <h4>DANIEL REYES</h4><div class="role">ATTORNEY</div>
    <div class="years">10 YEARS OF PRACTICE</div>
    <p>Lorem ipsum dolor sit amet, consectetur adipiscing elit, sed do eiusmod tempor incididunt ut labore et dolore magna aliqua. Ut enim ad minim veniam, quis nostrud exercitation ullamco laboris nisi ut aliquip ex ea commodo consequat.</p>
    <div class="more">More &#8250;</div>
  </div>

  <div class="attorney-photo abs" style="left:613px;top:2218px" role="img" aria-label="Portrait of attorney Martin Hale"></div>
  <div class="attorney abs" style="left:882px;top:2218px">
    <h4>MARTIN HALE</h4><div class="role">ATTORNEY</div>
    <div class="years">12 YEARS OF PRACTICE</div>
    <p>Lorem ipsum dolor sit amet, consectetur adipiscing elit, sed do eiusmod tempor incididunt ut labore et dolore magna aliqua. Ut enim ad minim veniam, quis nostrud exercitation ullamco laboris nisi ut aliquip ex ea commodo consequat.</p>
    <div class="more">More &#8250;</div>
  </div>
</section>

<footer>
  <div class="social-bar abs">
    <span><i class="social-dot"></i>FOLLOW US ON FRIENDSPACE</span>
    <span><i class="social-dot"></i>FOLLOW US ON CHIRPER</span>
  </div>
  <div class="footer-main abs"></div>
  <div class="footer-col abs" style="left:73px">
    <h5>COME AND VISIT</h5>
    <p>Meridian Law Group<br>Harbor Point Office Suite<br>Riverton, LA 70000<br><b>View on CityMaps</b></p>
  </div>
  <div class="footer-col abs" style="left:433px">
    <h5>GET IN TOUCH</h5>
    <p><b>555-014-2290</b><br><b>info@meridianlawgroup.com</b></p>
  </div>
  <div class="footer-col abs" style="left:793px">
    <h5>STAY INFORMED</h5>
    <div class="subscribe">
      <div class="input">Enter email address</div>
      <svg class="go" viewBox="0 0 42 42"><path d="M17 13l8 8-8 8" fill="none" stroke="#fff" stroke-width="3"/></svg>
    </div>
  </div>
  <div class="footer-bottom abs">
    <span>&copy; 2016 Meridian Law Group. All rights reserved.</span>
    <nav><span>Home</span><span>Privacy</span><span>Terms of Service</span><span>Contact</span></nav>
  </div>
</footer>

</body>
</html>
```